Re-Brand of TindelMox along with a new website design

TindelMox Ltd are a software & database development company using technologies such as PHP, C#, HTML, JQuery, Flex, AS3, MySQL, Oracle, MSSQL. We like to target all types of business from small to large.

We are great at coding but rubbish at design so thats where we need your help!

We want a complete re-brand of TindelMox including logo, website design, and business cards.

We would like a design that is clean but other than that, please feel free to be creative.

****Logo****
We are looking for a logo that appears professional but with a splash of colour that indicates a creative side. Please see below some logos that we like the look of:

We like this one because it has a nice simple and clear font for the name of the company but also an icon which is colourful and stands out. http://markvault.example/2013/03/brivelo/

We like this one because it is very clean, simple and again very clear. http://markvault.example/2013/03/quantorels/

http://markvault.example/2013/03/tide-lamp/
http://markvault.example/2013/02/velmorin/
http://markvault.example/2013/01/art-gallery-tarnwick/

As you will see from all of these examples, the font is very clear but there is always a graphic representing the company too. This is what we like.

****Website****
These are some of the examples of websites we like:
https://www.zestrune.example/
https://www.chatterlane.example/home
http://www.haldenimagery.example/
http://www.vistor.example/
http://quillbay.example/
https://www.usebriefnest.example/personal-intros
http://www.marmotpanel.example/

The current site can be found at tindelmox.example.uk

Reason: We have extended the deadline of the project by 5 days as I realise the original deadline was very tight.

Software

Requirements
Must have
• Website must have the following pages
Home
Services
Projects
About Us
Contact Us

```html
<!DOCTYPE html>
<html lang="en">
<head>
<meta charset="utf-8">
<title>TindelMox Business Card</title>
<link href="https://fonts.googleapis.com/css2?family=Lato:wght@300;400&display=swap" rel="stylesheet">
<style>
  :root {
    --page: #ffffff;
    --card: #2c333e;
    --accent: #0fe93a;
    --accent-text: #1fc43a;
    --ink: #ffffff;
  }
  * { margin: 0; padding: 0; box-sizing: border-box; }
  html, body { width: 912px; height: 1200px; overflow: hidden; background: var(--page); }
  body { position: relative; font-family: "Lato", sans-serif; color: var(--ink); }

  .card {
    position: absolute; left: 52px; width: 808px; height: 504px;
    background: var(--card); overflow: hidden;
  }
  .card--front { top: 54px; }
  .card--back { top: 642px; }

  .accent-bar { position: absolute; height: 10px; width: 190px; background: var(--accent); }
  .accent-bar--top { top: 0; border-radius: 0 0 7px 7px; }
  .accent-bar--bottom { bottom: 0; border-radius: 7px 7px 0 0; }
  .card--front .accent-bar--top { left: 576px; }
  .card--front .accent-bar--bottom { left: 40px; }
  .card--back .accent-bar--top { left: 38px; }
  .card--back .accent-bar--bottom { left: 577px; }

  .brand-dot {
    position: absolute; left: 354px; top: 110px; width: 100px; height: 100px;
    border-radius: 50%; background: var(--accent);
  }
  .brand-name {
    position: absolute; left: 0; right: 0; top: 340px; text-align: center;
    font-weight: 300; font-size: 76px; line-height: 1; letter-spacing: 1px;
    color: var(--ink);
  }
  .brand-url {
    position: absolute; left: 343px; top: 434px; height: 34px; padding: 0 14px;
    background: var(--accent); border-radius: 7px;
    font-size: 19px; line-height: 34px; color: var(--ink);
  }

  .person-name {
    position: absolute; left: 37px; top: 112px;
    font-weight: 300; font-size: 45px; line-height: 1;
  }
  .person-role {
    position: absolute; left: 37px; top: 161px;
    font-weight: 300; font-size: 17px; color: var(--accent-text);
  }

  .contact-list { position: absolute; right: 28px; top: 292px; list-style: none; }
  .contact-item {
    display: flex; justify-content: flex-end; align-items: center;
    height: 22px; margin-bottom: 22px; font-size: 17px;
  }
  .contact-item span { margin-right: 24px; }
  .contact-icon { width: 20px; height: 20px; fill: var(--ink); }
</style>
</head>
<body>
  <section class="card card--front">
    <div class="accent-bar accent-bar--top"></div>
    <div class="brand-dot"></div>
    <h1 class="brand-name">TINDELMOX</h1>
    <div class="brand-url">www.tindelmox.example.uk</div>
    <div class="accent-bar accent-bar--bottom"></div>
  </section>

  <section class="card card--back">
    <div class="accent-bar accent-bar--top"></div>
    <h2 class="person-name">John Doe</h2>
    <p class="person-role">Designation</p>
    <ul class="contact-list">
      <li class="contact-item">
        <span>01632 960 418</span>
        <svg class="contact-icon" viewBox="0 0 20 20"><path d="M6 1h8a2 2 0 0 1 2 2v14a2 2 0 0 1-2 2H6a2 2 0 0 1-2-2V3a2 2 0 0 1 2-2zm0 2.5v11h8v-11zM10 15.6a1 1 0 1 0 0 2 1 1 0 0 0 0-2z"/></svg>
      </li>
      <li class="contact-item">
        <span>contact@tindelmox.example.uk</span>
        <svg class="contact-icon" viewBox="0 0 20 20"><path d="M2 4h16v1.5L10 11 2 5.5z"/><path d="M2 7.5l5 3.5-5 4.5zM18 7.5v8l-5-4.5zM8.2 11.8L10 13l1.8-1.2L17 16H3z"/></svg>
      </li>
      <li class="contact-item">
        <span>42 Fernbrook Lane, Calderwick, Marlshire, CW4 7QT</span>
        <svg class="contact-icon" viewBox="0 0 20 20"><path d="M10 1a6 6 0 0 0-6 6c0 4.5 6 12 6 12s6-7.5 6-12a6 6 0 0 0-6-6zm0 8.3A2.3 2.3 0 1 1 10 4.7a2.3 2.3 0 0 1 0 4.6z"/></svg>
      </li>
    </ul>
    <div class="accent-bar accent-bar--bottom"></div>
  </section>
</body>
</html>
```